Trade Show Poster/Booth Backdrop for Rugged Technology Business

I need a graphic design for an 8' x 6' poster to hang on back wall of my event booth. Design must be consistent with my company's colors, logo, and current branding as shown on website, Facebook, and Twitter (links provided). You can propose other elements, but there are certain core images and text elements that must be incorporated. Print specifications also provided. File must be delivered on time and upload-ready.

Font styles to use
Sans Serif

Colors
33a6d7
0355a3
33b8a4
00a990
9bcb3b
abd036
cadf82
85cae6
86cfc6

Requirements
Nice to have
• Regarding color, I'm okay with designs using the orange version of the Vorlin logo.
• Regarding the images I provided as potential background layers, I especially like the ones with rocky island profiles and exposed cliff faces. In addition to being a nice match color wise, they are subtle suggestions of ruggedness and working with technology that can handle extreme environments (which is a big part of the messaging focus).
Should not have
• Vibrant coloration is very much desired and OK, but please avoid a blend that goes to either extreme. For instance, too much dark blue makes it look like every other tech company ever. Too much warm, light green (other than for contrast elements) makes it look too tropical and casual.

```html
<!DOCTYPE html>
<html lang="en">
<head>
<meta charset="utf-8">
<title>Fully Rugged &amp; Business Class Technology Solutions</title>
<link rel="stylesheet" href="https://fonts.googleapis.com/css2?family=Work+Sans:wght@300;400;600&display=swap">
<style>
  :root {
    --deep-blue: #0355a3;
    --sky-blue: #33a6d7;
    --teal: #00a990;
    --sea-green: #33b8a4;
    --leaf-green: #2fae62;
    --white: #ffffff;
    --rule: rgba(255, 255, 255, 0.55);
    --font-main: "Work Sans", "Helvetica Neue", Arial, sans-serif;
  }
  * { margin: 0; padding: 0; box-sizing: border-box; }
  html, body {
    width: 900px;
    height: 1200px;
    overflow: hidden;
    background: #ffffff;
  }
  .poster {
    position: relative;
    width: 900px;
    height: 1200px;
    overflow: hidden;
    font-family: var(--font-main);
    color: var(--white);
  }
  .backdrop {
    position: absolute;
    inset: 0;
    background:
      linear-gradient(180deg, rgba(3, 60, 130, 0.35) 0%, rgba(3, 60, 130, 0) 45%, rgba(0, 80, 90, 0.25) 100%),
      linear-gradient(105deg, #1654a8 0%, #1b7fb6 30%, #1f9aa3 55%, #1ea77c 78%, #2aa65a 100%);
  }
  .backdrop::after {
    content: "";
    position: absolute;
    left: 0; right: 0;
    top: 600px; height: 320px;
    background: linear-gradient(180deg, rgba(255,255,255,0) 0%, rgba(200,240,235,0.14) 40%, rgba(255,255,255,0) 100%);
  }
  .headline {
    position: absolute;
    left: 103px;
    top: 104px;
    font-weight: 300;
    font-size: 58px;
    line-height: 70px;
    letter-spacing: 3px;
    text-transform: uppercase;
  }
  .offerings {
    position: absolute;
    left: 103px;
    top: 458px;
    list-style: none;
    font-weight: 400;
    font-size: 35px;
    line-height: 55px;
    letter-spacing: 1px;
  }
  .offerings li::before {
    content: "";
    display: inline-block;
    width: 9px;
    height: 9px;
    border-radius: 50%;
    background: var(--white);
    margin-right: 18px;
    vertical-align: middle;
    position: relative;
    top: -4px;
  }
  .brand-row {
    position: absolute;
    left: 100px;
    right: 100px;
    top: 950px;
    height: 86px;
    display: flex;
    align-items: center;
    justify-content: space-between;
  }
  .brand {
    display: flex;
    align-items: center;
    gap: 14px;
    font-weight: 600;
    font-size: 40px;
    letter-spacing: 1px;
  }
  .brand-mark {
    width: 64px;
    height: 64px;
    border-radius: 50%;
    border: 4px solid var(--white);
  }
  .brand--client { font-size: 34px; letter-spacing: 3px; }
  .divider {
    position: absolute;
    left: 100px;
    width: 698px;
    top: 1067px;
    height: 1px;
    background: var(--rule);
  }
  .contacts {
    position: absolute;
    left: 134px;
    right: 100px;
    top: 1088px;
    display: flex;
    gap: 62px;
    font-weight: 300;
    font-size: 22px;
  }
  .contact {
    display: flex;
    align-items: center;
    gap: 10px;
  }
  .contact-box {
    width: 24px;
    height: 24px;
    border-radius: 4px;
    background: var(--white);
  }
</style>
</head>
<body>
  <main class="poster">
    <div class="backdrop" role="img" aria-label="Photograph of a calm sea horizon with a rocky shoreline at lower left, tinted blue to green"></div>

    <h1 class="headline">Fully Rugged &amp;<br>Business Class<br>Technology<br>Solutions</h1>

    <ul class="offerings">
      <li>Mobility</li>
      <li>Computing</li>
      <li>Mounting</li>
      <li>Printing</li>
      <li>Imaging</li>
      <li>Storage</li>
    </ul>

    <div class="brand-row">
      <div class="brand brand--client"><span class="brand-mark"></span>MERIDIAN</div>
      <div class="brand">Vorlin</div>
      <div class="brand">Kestrel</div>
    </div>

    <div class="divider"></div>

    <div class="contacts">
      <div class="contact"><span class="contact-box"></span>MeridianforIT</div>
      <div class="contact"><span class="contact-box"></span>MeridianforIT</div>
      <div class="contact"><span class="contact-box"></span>meridiansystems.net</div>
    </div>
  </main>
</body>
</html>
```